EG 1 page flyer

I need a flyer design for a financial risk advisory business. I like the layout of the example on your site, for Corbin Delph (attached). Our business needs to show strength, safety, knowledge and security. We provide financial advice.

I have uploaded the front page of our larger brochure. I would like the man with the umbrella with the caption and the logo / brand on the front page, but with portrait orientation, instead of landscape.

For the second page (the back), I have got some ideas of the kinds of things I would want written on the attached Power Point. But it needs to be arranged better, with perhaps the Elsie's Gate Logo on there as well, to break up all the writing. Attached is an example of how it might look, but I want different formatting and layout ideas, that look better, more professional etc.

The page 1 comment what is elsies gate? predicting ......... would look better all the way along the bottom of the page, but i couldn't get the formatting right.

Financial

```html
<!DOCTYPE html>
<html lang="en">
<head>
<meta charset="utf-8">
<title>Elsie's Gate – Financial Risk Advisory Flyer</title>
<link rel="stylesheet" href="https://fonts.googleapis.com/css2?family=Source+Sans+3:wght@300;400;600;700&display=swap">
<style>
  :root {
    --page-bg: #ececec;
    --paper: #ffffff;
    --navy: #24275f;
    --sky: #00aeef;
    --ink-grey: #555a5f;
    --quote-ink: #1f2a5a;
    --photo-top: #5f6b58;
    --photo-mid: #7a8478;
    --photo-low: #4a4f5c;
  }
  * { box-sizing: border-box; margin: 0; padding: 0; }
  html, body {
    width: 1200px;
    height: 960px;
    overflow: hidden;
    background: var(--page-bg);
    font-family: "Source Sans 3", Arial, sans-serif;
  }
  .canvas {
    position: relative;
    width: 1200px;
    height: 960px;
  }
  .flyer {
    position: absolute;
    left: 288px;
    top: 38px;
    width: 568px;
    height: 803px;
    background: var(--paper);
    transform: scale(1.1);
    transform-origin: top left;
    box-shadow: 0 2px 10px rgba(0,0,0,0.12);
  }
  .brand {
    position: absolute;
    right: 52px;
    top: 78px;
    text-align: left;
  }
  .brand-line {
    display: flex;
    align-items: center;
    gap: 10px;
  }
  .brand-name {
    font-weight: 600;
    font-size: 40px;
    line-height: 1;
    color: var(--navy);
    letter-spacing: -0.5px;
  }
  .brand-dot {
    width: 14px;
    height: 14px;
    border-radius: 50%;
    background: var(--navy);
  }
  .brand-tagline {
    margin-top: 4px;
    font-size: 12.5px;
    color: var(--sky);
    word-spacing: 2px;
  }
  .brand-tagline span + span { margin-left: 10px; }
  .hero {
    position: absolute;
    left: 0;
    top: 146px;
    width: 568px;
    height: 342px;
    background:
      radial-gradient(ellipse at 35% 45%, rgba(30,30,35,0.55) 0%, rgba(30,30,35,0) 40%),
      linear-gradient(180deg, var(--photo-top) 0%, var(--photo-mid) 55%, var(--photo-low) 100%);
  }
  .hero-caption {
    position: absolute;
    left: 336px;
    top: 98px;
    font-weight: 300;
    font-size: 18px;
    line-height: 29px;
    color: #ffffff;
  }
  .service-band {
    position: absolute;
    left: 0;
    top: 499px;
    width: 568px;
    height: 37px;
    background: var(--sky);
    padding-left: 41px;
    display: flex;
    align-items: center;
  }
  .service-title {
    font-weight: 600;
    font-size: 20px;
    letter-spacing: 0.6px;
    color: #ffffff;
  }
  .service-list {
    position: absolute;
    left: 41px;
    top: 543px;
    display: flex;
    align-items: center;
    gap: 12px;
    font-size: 16px;
    letter-spacing: 0.3px;
    color: var(--ink-grey);
    list-style: none;
  }
  .service-list .drop-sep { width: 11px; height: 14px; }
  .motto {
    position: absolute;
    left: 0;
    top: 611px;
    width: 568px;
    height: 160px;
  }
  .motto-drop {
    position: absolute;
    left: 223px;
    top: 0;
    width: 122px;
    height: 154px;
  }
  .motto-text {
    position: absolute;
    left: 0;
    top: 79px;
    width: 568px;
    text-align: center;
  }
  .motto-question {
    font-weight: 700;
    font-size: 15px;
    color: #0077c0;
  }
  .motto-quote {
    font-size: 15.5px;
    color: var(--quote-ink);
    margin-top: 1px;
  }
</style>
</head>
<body>
<main class="canvas">
  <article class="flyer">
    <header class="brand">
      <div class="brand-line">
        <span class="brand-name">Elsie's Gate</span>
        <span class="brand-dot" aria-hidden="true"></span>
      </div>
      <p class="brand-tagline"><span>Our experience</span><span>Your edge</span></p>
    </header>

    <section class="hero" role="img" aria-label="Photograph of a man in a bowler hat holding an umbrella, walking down a rainy tree-lined street">
      <p class="hero-caption">Whatever the<br>financial forecast…<br>it pays to<br>be prepared!</p>
    </section>

    <div class="service-band">
      <h1 class="service-title">FINANCIAL RISK ADVISORY</h1>
    </div>

    <ul class="service-list">
      <li>DEBT &amp; FUNDING</li>
      <li><svg class="drop-sep" viewBox="0 0 11 14" aria-hidden="true"><path d="M5.5 0 L10 7 A5 5 0 1 1 1 7 Z" fill="var(--sky)"/></svg></li>
      <li>MARKET RISK</li>
      <li><svg class="drop-sep" viewBox="0 0 11 14" aria-hidden="true"><path d="M5.5 0 L10 7 A5 5 0 1 1 1 7 Z" fill="var(--sky)"/></svg></li>
      <li>ACTIVE ENGAGEMENT</li>
    </ul>

    <section class="motto">
      <svg class="motto-drop" viewBox="0 0 122 154" aria-hidden="true">
        <path d="M61 0 L108 54 A61 61 0 1 1 14 54 Z" fill="var(--sky)"/>
        <rect x="0" y="70" width="122" height="59" fill="var(--paper)"/>
      </svg>
      <div class="motto-text">
        <p class="motto-question">What is Elsie's Gate?</p>
        <p class="motto-quote">“Predicting rain doesn’t count; building arks does”.</p>
      </div>
    </section>
  </article>
</main>
</body>
</html>
```